Darlene Whitcott

I need all of my logos on one card. I would like a burgundy back and Harbor Shield and Tamsworth insurance being the most prominent.
Phone Number 541-382-9154
Web:
www.Tamsworthins.example
www.Harbor Shield.example
www.Kell-Insurance.example

```html
<!DOCTYPE html>
<html lang="en">
<head>
<meta charset="utf-8">
<title>Darlene Whitcott – Business Card</title>
<link rel="stylesheet" href="https://fonts.googleapis.com/css2?family=Cinzel:wght@500;700&family=Lato:wght@400&display=swap">
<style>
  :root {
    --backdrop: #656565;
    --burgundy: #4a1418;
    --burgundy-deep: #3c0f13;
    --ink-light: #f4eeee;
    --rule: rgba(255, 255, 255, 0.35);
    --gold: #d9a21c;
  }
  html, body {
    margin: 0;
    width: 1200px;
    height: 900px;
    overflow: hidden;
    background: var(--backdrop);
  }
  .canvas {
    position: relative;
    width: 1200px;
    height: 900px;
  }
  .card {
    position: absolute;
    top: 275px;
    width: 478px;
    height: 295px;
    background: linear-gradient(160deg, var(--burgundy) 0%, var(--burgundy-deep) 100%);
  }
  .card--front {
    left: 120px;
    border-radius: 0 46px 0 46px;
  }
  .card--back {
    left: 620px;
    border-radius: 46px 0 46px 0;
  }
  .contact {
    position: absolute;
    left: 0;
    right: 0;
    top: 66px;
    text-align: center;
    color: var(--ink-light);
    font-family: "Lato", sans-serif;
    font-size: 15px;
    line-height: 19px;
  }
  .contact__name {
    font-family: "Cinzel", serif;
    font-weight: 500;
    font-size: 20px;
    line-height: 24px;
    letter-spacing: 0.5px;
    margin: 0;
  }
  .contact__title { margin: 0 0 10px; }
  .contact__rule {
    width: 168px;
    height: 1px;
    background: var(--rule);
    border: 0;
    margin: 0 auto 11px;
  }
  .contact__group { margin: 0 0 12px; }
  .contact__group p { margin: 0; }
  .brand {
    position: absolute;
    font-family: "Cinzel", serif;
    font-weight: 700;
    color: var(--gold);
    text-align: center;
    line-height: 1.05;
    margin: 0;
  }
  .brand--tamsworth { left: 30px; top: 80px; width: 220px; font-size: 24px; }
  .brand--harbor { left: 262px; top: 80px; width: 190px; font-size: 26px; }
  .brand--kell { left: 86px; top: 232px; width: 146px; font-size: 15px; }
  .brand--farm { left: 250px; top: 232px; width: 150px; font-size: 15px; }
</style>
</head>
<body>
<main class="canvas">
  <section class="card card--front" aria-label="Card front">
    <div class="contact">
      <h1 class="contact__name">DARLENE WHITCOTT</h1>
      <p class="contact__title">Managing Director</p>
      <hr class="contact__rule">
      <div class="contact__group">
        <p>541-382-9154</p>
        <p>info@tamsworthins.example</p>
      </div>
      <hr class="contact__rule">
      <div class="contact__group">
        <p>www.Tamsworthins.example</p>
        <p>www.Harbor Shield.example</p>
        <p>www.Kell-Insurance.example</p>
      </div>
    </div>
  </section>

  <section class="card card--back" aria-label="Card back with agency names">
    <p class="brand brand--tamsworth">TAMSWORTH<br>INSURANCE</p>
    <p class="brand brand--harbor">HARBOR<br>SHIELD INC</p>
    <p class="brand brand--kell">KELL<br>AGENCY INC</p>
    <p class="brand brand--farm">TAMSWORTH<br>FARM &amp; RANCH</p>
  </section>
</main>
</body>
</html>
```